price list for web and print- sending to inquiring clients and use as promo material

Hello
I need a graphic design for my photography price list/s. I am a people photographer. The first of 6 price sheets will be for head shots- I would like a price sheet that captures the prospective clients' attention. The info and visual should be compelling and easy to digest. It should be simple yet interesting. I will provide you with some pictures but you do not have to include them. I have a studio indoors and outdoors also working on location. This design should be for email and print. The picture of "denise" is me and I use that on all my profiles. I like the fonts in the logo but it is too boxy and rigid

Target Market(s)

repeat client, word of mouth referrals, new people but aquaintances of others that might know me

Industry/Entity Type

Graphic Design

Font styles to use
Serif
Sans Serif
Script

Requirements
Must have
• prices and maybe some words about my services that I sent in... Please tie it together as best as possible..
Nice to have
• Loosen up my logo.. it is in a box.....contemporary design but not something that would not fit in with corporate.. I like this headline
• "Create a great first impression with your professional headshots"
• I sent in other copy and my logo(sent in the picture drop box)

```html
<!DOCTYPE html>
<html lang="en">
<head>
<meta charset="utf-8">
<title>Headshot Price Sheet</title>
<link href="https://fonts.googleapis.com/css2?family=Jost:wght@400;500;600;700&display=swap" rel="stylesheet">
<style>
  :root {
    --paper: #ffffff;
    --ink: #1b1b1b;
    --accent: #a5683a;
    --card: #f6f1e9;
    --pill: #111111;
    --pill-text: #ffffff;
  }
  * { box-sizing: border-box; margin: 0; padding: 0; }
  html, body {
    width: 1006px; height: 1200px; overflow: hidden;
    background: var(--paper);
    font-family: "Jost", "Helvetica Neue", Arial, sans-serif;
    color: var(--ink);
  }
  .sheet { position: relative; width: 1006px; height: 1200px; }

  .brand {
    position: absolute; left: 300px; top: 60px;
    display: flex; align-items: center; gap: 14px;
  }
  .brand-mark { width: 18px; height: 18px; background: var(--ink); }
  .brand-name { font-size: 26px; font-weight: 600; letter-spacing: 0.5px; color: var(--ink); }

  .headline {
    position: absolute; left: 70px; top: 140px; width: 866px;
    font-size: 36px; font-weight: 700; line-height: 1.15;
  }
  .headline .highlight { color: var(--accent); }

  .features {
    position: absolute; left: 70px; top: 250px; width: 866px;
    display: grid; grid-template-columns: repeat(3, 1fr); gap: 36px;
  }
  .feature-label {
    display: inline-block; background: var(--pill); color: var(--pill-text);
    font-size: 15px; font-weight: 600; padding: 2px 16px; border-radius: 4px;
    margin-bottom: 10px;
  }
  .feature-text { font-size: 16px; line-height: 1.3; color: var(--accent); }

  .price-title {
    position: absolute; left: 250px; top: 438px;
    font-size: 20px; font-weight: 700;
  }

  .pricing {
    position: absolute; left: 250px; top: 480px; width: 690px;
    display: flex; gap: 30px; align-items: flex-start;
  }
  .pricing-column { width: 330px; display: flex; flex-direction: column; gap: 28px; }
  .pricing-column--offset { margin-top: -50px; }

  .package { background: var(--card); border-radius: 10px; padding: 22px 24px; }
  .package h2 { font-size: 22px; font-weight: 600; margin-bottom: 4px; }
  .package ul { list-style: none; font-size: 16px; line-height: 1.3; color: var(--accent); }
  .package .price { font-size: 22px; font-weight: 700; margin-top: 16px; }
  .package .extra { font-size: 15px; color: var(--accent); line-height: 1.3; }
  .package .extra strong { color: var(--ink); }

  .group-rates {
    position: absolute; left: 70px; top: 1060px; width: 866px;
    font-size: 17px; line-height: 1.3;
  }
  .group-rates .note { margin-bottom: 12px; }
</style>
</head>
<body>
<main class="sheet">
  <div class="brand">
    <span class="brand-mark"></span>
    <span class="brand-name">Denise M. Harlow Photography</span>
  </div>

  <h1 class="headline">Create a great first impression with your <span class="highlight">professional</span> headshots</h1>

  <section class="features">
    <div class="feature">
      <span class="feature-label">Experience</span>
      <p class="feature-text">Denise is an accomplished professional photographer who has helped thousands of clients. She is an expert at helping you look confident and approachable.</p>
    </div>
    <div class="feature">
      <span class="feature-label">24 Hour Turnaround</span>
      <p class="feature-text">Your time is valuable. Denise can complete the photoshoot in just 30 minutes (Or as long as you want). Our process is designed to save you time.</p>
    </div>
    <div class="feature">
      <span class="feature-label">Enjoyable</span>
      <p class="feature-text">You can look forward to an enjoyable photo session with Denise's professional guidance. Denise helps make the experience fun.</p>
    </div>
  </section>

  <h2 class="price-title">Price Sheet</h2>

  <section class="pricing">
    <div class="pricing-column">
      <article class="package package--entry">
        <h2>Entry Package</h2>
        <ul>
          <li>Quick and Simple</li>
          <li>One pose</li>
          <li>One wardrobe</li>
          <li>One selected image retouched</li>
        </ul>
        <p class="price">$175</p>
        <p class="extra">Additional images just <strong>$75</strong> each</p>
      </article>
      <article class="package package--premium">
        <h2>Premium Package</h2>
        <ul>
          <li>Get it all</li>
          <li>Four pose</li>
          <li>3-4 wardrobe</li>
          <li>4 selected image retouched</li>
          <li>2-3 background changes</li>
          <li>Optional outdoor studio</li>
        </ul>
        <p class="price">$525</p>
        <p class="extra">Additional images just <strong>$75</strong> each</p>
      </article>
    </div>
    <div class="pricing-column pricing-column--offset">
      <article class="package package--two-pose">
        <h2>2 Pose Package</h2>
        <ul>
          <li>Most Popular</li>
          <li>Two poses</li>
          <li>Two wardrobe</li>
          <li>Two selected image retouched</li>
          <li>One or two background changes</li>
        </ul>
        <p class="price">$175</p>
        <p class="extra">Additional images just <strong>$75</strong> each</p>
      </article>
      <article class="package package--location">
        <h2>At your location</h2>
        <ul>
          <li>Minimum of 5 people</li>
          <li>One selected image retouched</li>
        </ul>
        <p class="price">$250</p>
        <p class="extra">Additional images just <strong>$50</strong> each</p>
      </article>
    </div>
  </section>

  <section class="group-rates">
    <p class="note">If possible, we like 1/2 hour appts for each person so they can view their images on the computer</p>
    <p>5-10 people <strong>$150</strong> EACH</p>
    <p>11-20 people <strong>$100</strong> each</p>
    <p>20+ <strong>$75</strong> each</p>
  </section>
</main>
</body>
</html>
```